New Brochure for existing Virtual Reality Amusement Arena

I need a two sided half page brochure for my arcade. it needs to say what we do and what we have to offer. It basically needs to be a paper copy of all the information thats on my website www.kavimo-nix.com
Please check that as it is very informative!
Industry/Entity Type
Entertainment
Colors
Designer to choose colors to be used in the design.
Requirements
Must have
- Color. I have uploaded an old brochure I had made, but now we have a new company and new logo, please make it similar to that. Please pull all pics from my website www.kavimo-nix.com
Should not have
- useless information

```html
<!DOCTYPE html>
<html lang="en">
<head>
<meta charset="utf-8">
<title>Kavimo-Nix Brochure</title>
<link rel="stylesheet" href="https://fonts.googleapis.com/css2?family=Roboto+Condensed:wght@700&family=Open+Sans:wght@400;600;700&display=swap">
<style>
  :root{
    --red:#c21e2e;
    --red-deep:#7e1420;
    --blue:#2432b8;
    --blue-deep:#141c6e;
    --smoke:#b8bcd4;
    --white:#ffffff;
    --ink:#1a1a1a;
    --bar:#2b2b2b;
  }
  *{margin:0;padding:0;box-sizing:border-box}
  html,body{width:900px;height:1200px;overflow:hidden;background:var(--white)}
  .canvas{position:relative;width:900px;height:1200px;background:var(--white)}
  .brochure{position:absolute;left:42px;top:75px;width:803px;height:568px;overflow:hidden}
  .panel{position:absolute;top:0;height:568px;overflow:hidden}
  .panel--front{left:0;width:402px}
  .panel--back{left:402px;width:401px}
  .panel-bg{position:absolute;inset:0;width:100%;height:100%}

  .headline{position:absolute;left:40px;color:var(--white);font-family:"Roboto Condensed",sans-serif;font-weight:700;text-transform:uppercase;line-height:1}
  .headline--lead{top:64px;font-size:33px;letter-spacing:.5px}
  .headline--main{top:102px;font-size:50px;letter-spacing:.5px}

  .intro{position:absolute;left:40px;top:162px;width:340px;color:var(--white);font-family:"Open Sans",sans-serif;font-weight:600;font-size:11.5px;line-height:1.3}

  .entry-box{position:absolute;left:36px;top:224px;width:326px;height:56px;border:3px solid var(--white);padding:6px 20px 0 24px;color:var(--white);font-family:"Open Sans",sans-serif;font-weight:600;font-size:11.5px;line-height:1.3}
  .entry-box::before{content:"";position:absolute;left:10px;right:10px;top:-3px;bottom:-3px;background:transparent;border-top:3px solid rgba(0,0,0,0);}
  .entry-box .mask{position:absolute;left:10px;right:10px;top:-3px;height:3px}
  .entry-box .mask--bottom{top:auto;bottom:-3px}

  .photo{position:absolute}
  .photo--player-front{left:258px;top:300px;width:116px;height:268px;background:linear-gradient(180deg,#d0d0d0,#8e8e8e 55%,#5a5a5a);border-radius:40px 40px 6px 6px}
  .photo--player-back{left:178px;top:55px;width:223px;height:450px;background:linear-gradient(160deg,rgba(170,40,55,.85),rgba(120,20,35,.9) 60%,rgba(200,120,130,.6));border-radius:90px 30px 0 0}

  .contact-band{position:absolute;left:0;bottom:0;width:402px;height:73px;background:var(--red-deep)}
  .contact-band .phone{position:absolute;left:36px;top:20px;color:var(--white);font-family:"Open Sans",sans-serif;font-weight:600;font-size:13.5px}
  .contact-band .address{position:absolute;left:36px;top:42px;color:var(--white);font-family:"Open Sans",sans-serif;font-weight:600;font-size:11px}

  .brand{position:absolute;left:52px;top:30px;display:flex;align-items:center;gap:8px;color:var(--white);font-family:"Roboto Condensed",sans-serif;font-weight:700;font-size:26px;letter-spacing:1px}
  .brand .mark{width:24px;height:24px;border-radius:50%;background:var(--white)}

  .tagline{position:absolute;left:20px;top:172px;color:var(--white);font-family:"Roboto Condensed",sans-serif;font-weight:700;font-size:52px;line-height:.93;text-transform:uppercase;letter-spacing:.5px;text-shadow:0 2px 6px rgba(0,0,0,.35)}

  .footer-area{position:absolute;left:0;bottom:0;width:401px;height:62px;background:var(--white)}
  .footer-area .summary{position:absolute;left:53px;top:12px;width:330px;color:var(--ink);font-family:"Open Sans",sans-serif;font-weight:600;font-size:7.4px;line-height:1.35}
  .web-bar{position:absolute;right:0;bottom:0;width:160px;height:18px;background:var(--bar);color:var(--white);font-family:"Open Sans",sans-serif;font-weight:600;font-size:8px;letter-spacing:1.5px;line-height:18px;text-align:center}
</style>
</head>
<body>
<div class="canvas">
  <div class="brochure">

    <section class="panel panel--front">
      <svg class="panel-bg" viewBox="0 0 402 568" preserveAspectRatio="none" aria-hidden="true">
        <defs>
          <radialGradient id="front-smoke" cx="0.65" cy="0.55" r="0.6">
            <stop offset="0" stop-color="#c9cce0" stop-opacity=".9"/>
            <stop offset="1" stop-color="#c9cce0" stop-opacity="0"/>
          </radialGradient>
        </defs>
        <rect width="402" height="568" fill="#2632b0"/>
        <polygon points="0,90 240,568 0,568" fill="#c21e2e"/>
        <polygon points="0,230 170,568 110,568 0,350" fill="#e0263a" opacity=".8"/>
        <polygon points="60,0 402,500 402,568 330,568 0,80 0,0" fill="#1a2390" opacity=".45"/>
        <polygon points="150,0 402,320 402,380 110,0" fill="#3b49d0" opacity=".5"/>
        <rect width="402" height="568" fill="url(#front-smoke)"/>
      </svg>

      <h1 class="headline headline--lead">Gaming like you’ve</h1>
      <h1 class="headline headline--main">Never seen</h1>
      <p class="intro">Home of Tampa's one of a kind video game experience. Fully immersive VR, state of the art tech. A completely new play experience for everyone!</p>

      <p class="entry-box" style="border-top-color:transparent;border-bottom-color:transparent;border-left-width:3px;border-right-width:3px">
        Just walk right in. Up to eight people can enter at once at stay to try all our products. A new group comes in every 2 hours. Group and entrance times are as follows
      </p>
      <svg style="position:absolute;left:36px;top:224px" width="326" height="56" aria-hidden="true">
        <polyline points="10,1.5 1.5,1.5 1.5,54.5 10,54.5" fill="none" stroke="#fff" stroke-width="3"/>
        <polyline points="316,1.5 324.5,1.5 324.5,54.5 316,54.5" fill="none" stroke="#fff" stroke-width="3"/>
      </svg>

      <div class="contact-band">
        <p class="phone">CALL US TODAY-813.555.0142</p>
        <p class="address">2150 W Harbor Ln, Tampa FL 33607</p>
      </div>

      <div class="photo photo--player-front" role="img" aria-label="Black and white photo of a woman wearing a VR headset holding motion controllers"></div>
    </section>

    <section class="panel panel--back">
      <svg class="panel-bg" viewBox="0 0 401 568" preserveAspectRatio="none" aria-hidden="true">
        <defs>
          <radialGradient id="back-smoke" cx="0.7" cy="0.7" r="0.55">
            <stop offset="0" stop-color="#f2c5cb" stop-opacity=".8"/>
            <stop offset="1" stop-color="#f2c5cb" stop-opacity="0"/>
          </radialGradient>
        </defs>
        <rect width="401" height="568" fill="#9c1a2a"/>
        <polygon points="0,0 120,0 401,420 401,568 300,568 0,120" fill="#b8202f"/>
        <polygon points="0,260 160,568 0,568" fill="#2a36c0"/>
        <polygon points="0,150 220,568 180,568 0,230" fill="#3a47d4" opacity=".7"/>
        <polygon points="240,0 401,0 401,200" fill="#c8303e" opacity=".6"/>
        <rect width="401" height="568" fill="url(#back-smoke)"/>
      </svg>

      <div class="photo photo--player-back" role="img" aria-label="Red-tinted photo of a man wearing a VR headset and backpack holding controllers"></div>

      <div class="brand"><span class="mark"></span>KAVIMO-NIX</div>

      <h2 class="tagline">Because<br>that’s<br>where<br>all the<br>fun is</h2>

      <div class="footer-area">
        <p class="summary">A virtual reality amusement park and video game lounge. Incorporating the love of video games with state-of-the-art-tech, this is GAMING LIKE YOU'VE NEVER SEEN</p>
        <p class="web-bar">www.kavimo-nix.com</p>
      </div>
    </section>

  </div>
</div>
</body>
</html>
```